Coral Ridge Networks Ltd

I need a website that is an informational only. We are a construction business building telecommunications sites. Seeing how our company is Coral Ridge the color blue might want to be incorporated in the color scheme.
I can provide more picture of towers and wireless communications if needed.
current website www.coralridgenet.ca

Industry/Entity Type

Wireless Telecommunications, Construction

Coding

Coded - Design and coding required

Number of Pages Required

2 page

Font styles to use
Sans Serif

Colors

Designer to choose colors to be used in the design.

```html
<!DOCTYPE html>
<html lang="en">
<head>
<meta charset="utf-8">
<title>Coral Ridge Networks Ltd</title>
<link href="https://fonts.googleapis.com/css2?family=Mulish:ital,wght@0,400;0,500;0,600;0,700;1,500&family=Courgette&display=swap" rel="stylesheet">
<style>
:root{
  --blue:#3d72bb;
  --blue-dark:#2f52a0;
  --blue-light:#5ea8df;
  --ink:#222;
  --text:#444;
  --grey-bg:#f1f1f1;
  --white:#fff;
}
*{box-sizing:border-box;margin:0;padding:0}
html,body{width:1200px;height:3368px;overflow:hidden}
body{position:relative;background:var(--white);font-family:'Mulish',sans-serif;color:var(--text)}
.abs{position:absolute}
.logo{display:flex;align-items:center;gap:10px;font-size:34px;font-weight:600;color:var(--blue);font-family:'Mulish',sans-serif}
.logo .dot{width:22px;height:22px;border-radius:50%;background:var(--blue)}
.photo{position:absolute}
.btn-solid{position:absolute;display:flex;align-items:center;justify-content:center;color:var(--white);font-size:17px;background:linear-gradient(90deg,var(--blue-light),var(--blue-dark))}
.btn-white{position:absolute;display:flex;align-items:center;justify-content:center;gap:12px;background:var(--white);color:var(--blue-dark);font-size:19px;font-weight:500}
.section-title{position:absolute;left:0;width:1200px;text-align:center;font-size:48px;font-weight:500;color:var(--blue)}
.rule{position:absolute;height:2px;background:var(--blue)}
.hero-title{left:99px;top:256px;font-size:38px;line-height:51px;color:var(--ink);font-weight:500}
.top-contact{left:752px;top:39px;width:120px;height:47px;background:var(--white);color:var(--ink);font-size:17px;display:flex;align-items:center;justify-content:center}
.top-email{left:920px;top:44px;color:var(--white);font-size:13px;line-height:20px;display:flex;gap:12px;align-items:center}
.intro{left:98px;top:780px;width:440px;font-size:15.5px;line-height:27.5px;color:#333}
.intro p+p{margin-top:4px}
.script{font-family:'Courgette',cursive;color:var(--blue);font-size:22px}
.checklist{left:593px;top:772px;width:502px;height:373px;background:var(--white);box-shadow:0 2px 12px rgba(0,0,0,.08);padding:44px 30px 0 28px;list-style:none;font-size:15.5px;color:#333}
.checklist li{display:flex;gap:20px;line-height:27px;margin-bottom:12px}
.checklist li::before{content:'›';color:var(--blue);font-size:20px;line-height:24px}
.services-bg{left:0;top:1230px;width:1200px;height:1255px;background:var(--grey-bg)}
.service h3{font-size:22px;font-weight:500;color:var(--ink)}
.service .line{width:52px;height:2px;background:var(--blue);margin:10px 0 16px}
.service p{font-size:17px;line-height:31px;color:#333}
.side-bar{position:absolute;width:4px;background:var(--blue)}
.about p{font-size:15.5px;line-height:29px;color:#444;margin-bottom:6px}
.about .lead{font-style:italic;color:var(--blue);font-size:17.5px;line-height:31px;font-weight:500}
.footer{left:0;top:3141px;width:1200px;height:227px;background:linear-gradient(100deg,#5aaae0,#3457a0)}
.footer .item{position:absolute;top:60px;display:flex;gap:12px;color:var(--white);font-size:14px;line-height:22px}
</style>
</head>
<body>

<!-- Hero -->
<div class="abs logo" style="left:98px;top:52px"><span class="dot"></span>Coral Ridge</div>
<div class="photo" role="img" aria-label="Rooftop telecom antenna mounts on steel frames under a blue sky" style="left:573px;top:0;width:627px;height:597px;background:linear-gradient(180deg,#4c6cb5 0%,#7d93c9 45%,#9ea4a6 70%,#6f7270 100%)"></div>
<div class="abs top-contact">Contact Us</div>
<div class="abs top-email">
  <svg width="26" height="22" viewBox="0 0 26 22" fill="none" stroke="#fff" stroke-width="1.6"><rect x="1" y="6" width="24" height="15"/><path d="M1 6l12 9 12-9M5 6V1h16v5"/></svg>
  <div>Email Us<br>info@coralridgenet.ca</div>
</div>
<h1 class="abs hero-title">We Are A In Construction<br>Business Building For<br>Telecommunications Firms</h1>
<div class="btn-solid" style="left:98px;top:423px;width:120px;height:46px">Contact Us</div>

<!-- Why choose us -->
<h2 class="section-title" style="top:654px">Why Choose Us</h2>
<div class="rule" style="left:554px;top:727px;width:22px"></div>
<div class="rule" style="left:580px;top:727px;width:62px"></div>

<div class="abs intro">
  <p>At Coral Ridge Networks Ltd Safety is number one. Coral Ridge Ltd is committed to a strong safety policy, protecting its staff and the general public from accidents and harm. All Coral Ridge Employees are certified “Tower Competent Climber and Rescue”.</p>
  <p>In addition to tower safety and fall protection Coral Ridge’s safety training and practices include but are not limited to the following:</p>
  <p class="script" style="margin:14px 0 0 5px">To Get Your Work Done</p>
</div>
<div class="btn-solid" style="left:98px;top:1069px;width:390px;height:63px;gap:14px;font-size:19px">
  <svg width="26" height="26" viewBox="0 0 26 26" fill="none" stroke="#fff" stroke-width="1.6"><path d="M6 3l4 5-2 3c1 3 4 6 7 7l3-2 5 4-3 4C11 24 2 15 2 7z"/><path d="M15 6a6 6 0 0 1 5 5M15 2a10 10 0 0 1 9 9"/></svg>
  Contact Us Today 1-604-555-0182
</div>

<ul class="abs checklist">
  <li>COR Certified</li>
  <li>BC Level 1 first aid</li>
  <li>Transportation Endorsement first aid</li>
  <li>Rope Access Level 1</li>
  <li>On site tailboard meeting with daily checklist sign<br>off and picture documentation</li>
  <li>Monthly in office safety meetings</li>
  <li>Job site specific hazard assessment and reporting</li>
</ul>

<!-- Services -->
<div class="abs services-bg"></div>
<h2 class="section-title" style="top:1303px">Our Services</h2>
<div class="rule" style="left:554px;top:1367px;width:22px"></div>
<div class="rule" style="left:580px;top:1367px;width:62px"></div>

<div class="abs service" style="left:99px;top:1488px;width:480px">
  <h3>Rooftop Sites</h3><div class="line"></div>
  <p>Structural upgrades or simple ballast mounts. Shelter on the ground, leasehold build outs or cabinets on the roof. Coral Ridge can install what you need where you need it.</p>
</div>
<div class="side-bar" style="left:620px;top:1483px;height:144px"></div>
<div class="photo" role="img" aria-label="Rooftop antenna site with mountains behind" style="left:625px;top:1410px;width:472px;height:291px;background:linear-gradient(180deg,#5b7fc8 0%,#8ea3c9 45%,#c3c7cb 70%,#7a7d80 100%)"></div>

<div class="photo" role="img" aria-label="Cell tower monopole against a clear sky" style="left:97px;top:1702px;width:472px;height:291px;background:linear-gradient(180deg,#88aee7,#a4c1ec)"></div>
<div class="side-bar" style="left:569px;top:1774px;height:145px"></div>
<div class="abs service" style="left:627px;top:1778px;width:470px">
  <h3>Towers and Monopoles</h3><div class="line"></div>
  <p>Coral Ridge can engineer, supply and install all your tower needs. New structures or existing, call us for pricing we would be happy to help out.</p>
</div>

<div class="abs service" style="left:98px;top:2071px;width:480px">
  <h3>In Building</h3><div class="line"></div>
  <p>Small office or large Hotel.&nbsp; Coral Ridge has installed services into all size buildings. Fiber, cat6, or coax, we have the abilities to install, test, and get the job done.</p>
</div>
<div class="side-bar" style="left:620px;top:2066px;height:146px"></div>
<div class="photo" role="img" aria-label="Antennas mounted on top of a red brick building" style="left:625px;top:1993px;width:472px;height:292px;background:linear-gradient(180deg,#e6e8ee 0%,#d9dbe2 55%,#c0604a 70%,#a8503d 100%)"></div>

<div class="btn-white" style="left:403px;top:2355px;width:391px;height:63px">
  <svg width="26" height="26" viewBox="0 0 26 26" fill="none" stroke="#2f52a0" stroke-width="1.6"><path d="M6 3l4 5-2 3c1 3 4 6 7 7l3-2 5 4-3 4C11 24 2 15 2 7z"/><path d="M15 6a6 6 0 0 1 5 5M15 2a10 10 0 0 1 9 9"/></svg>
  Contact Us Today 1-604-555-0182
</div>

<!-- About -->
<div class="photo" role="img" aria-label="Fenced equipment compound with chain-link fence" style="left:97px;top:2571px;width:341px;height:410px;background:linear-gradient(180deg,#4a7fd0 0%,#93aedb 45%,#9d9a93 75%,#7d7a74 100%)"></div>
<div class="photo" role="img" aria-label="Portrait of the company owner" style="left:312px;top:2807px;width:243px;height:251px;border:4px solid #fff;background:linear-gradient(160deg,#2e3b24,#6d6a58)"></div>
<div class="abs" style="left:316px;top:2990px;width:235px;text-align:center;color:#fff;font-family:'Courgette',cursive;font-size:21px;line-height:26px">Daniel R. Hart<br><span style="font-size:17px">Owner</span></div>

<h2 class="abs" style="left:575px;top:2603px;font-size:48px;font-weight:500;color:var(--blue)">About Us</h2>
<div class="rule" style="left:576px;top:2668px;width:22px"></div>
<div class="rule" style="left:602px;top:2668px;width:62px"></div>
<div class="abs about" style="left:575px;top:2694px;width:520px">
  <p>At Coral Ridge Ltd, we are dedicated to providing our customers with friendly professional service. We value your business.</p>
  <p>We have made it our mission to provide reliable products and services in our customer-driven approach.</p>
  <p>Our courteous, professional team is able to support a range of services to meet your requirements.</p>
  <p class="lead">To Learn More About Coral Ridge Ltd, And The Products And Services We Can Offer, Please Call Us At 1-604-555-0182.</p>
</div>
<div class="btn-solid" style="left:575px;top:2968px;width:119px;height:46px;background:var(--blue-dark)">Contact Us</div>

<!-- Footer -->
<footer class="abs footer">
  <div class="abs logo" style="left:98px;top:82px;color:#fff"><span class="dot" style="background:#fff"></span>Coral Ridge</div>
  <div class="item" style="left:399px">
    <svg width="22" height="30" viewBox="0 0 22 30" fill="none" stroke="#fff" stroke-width="1.6"><path d="M11 29S2 17 2 11a9 9 0 0 1 18 0c0 6-9 18-9 18z"/><circle cx="11" cy="11" r="3.5"/></svg>
    <div>4150 Maple Crest Ave<br>Surrey, BC V3S1K2</div>
  </div>
  <div class="item" style="left:664px">
    <svg width="30" height="30" viewBox="0 0 26 26" fill="none" stroke="#fff" stroke-width="1.5"><path d="M6 3l4 5-2 3c1 3 4 6 7 7l3-2 5 4-3 4C11 24 2 15 2 7z"/><path d="M15 6a6 6 0 0 1 5 5M15 2a10 10 0 0 1 9 9"/></svg>
    <div>Call Us<br>1-604-555-0182</div>
  </div>
  <div class="item" style="left:886px">
    <svg width="26" height="24" viewBox="0 0 26 22" fill="none" stroke="#fff" stroke-width="1.6"><rect x="1" y="6" width="24" height="15"/><path d="M1 6l12 9 12-9M5 6V1h16v5"/></svg>
    <div>Email Us<br>info@coralridgenet.ca</div>
  </div>
  <div class="abs" style="left:399px;top:123px;width:696px;height:1px;background:rgba(255,255,255,.5)"></div>
  <div class="abs" style="left:399px;top:141px;color:#fff;font-size:14px">©2022. Coral Ridge Networks Ltd.&nbsp; All Rights Reserved</div>
</footer>

</body>
</html>
```